Consulting, Investors, Joint Venture Website

Founded in April 2018, Marendo Advisers Limited (MAL) is an advisory consulting firm specializing in engaging investors in business ventures in Tanzania.
With extensive experience in construction, energy, oil and gas and the legal professions, our team assembles our expertise that allows foreign investors to set foot and flourish in the Tanzanian market.
MAL is locally owned, founded and registered. Our shareholders are cultured Tanzanian citizens with extensive corporate experience in South Africa, Tanzania, United Kingdom and the United States.

Our mission is to provide responsive and unrivalled professional advice from learned and experienced professionals versed in the local market, with an understanding of the cultural and logistical challenges faced by foreign investors.

Our vision is to provide a complete investor’s package that initiates with company registration, compliance and documentation services and ultimately operational facilitation services.

Target Market(s)

Foreign Investors, International companies

Industry/Entity Type

Business Consultant

Number of Pages Required

5+ page

Requirements
Must have
• It will be 5 pages - Home, About Us, Services, Portfolio, Contact Us
Nice to have
• if it can look like https://www.vq-sample.com/
• or https://www.torvell.com or http://www.bramwickpoint.com/

```html
<!DOCTYPE html>
<html lang="en">
<head>
<meta charset="utf-8">
<title>Marendo Advisers Limited</title>
<link href="https://fonts.googleapis.com/css2?family=Lora:wght@400&family=Figtree:wght@400;600;700&display=swap" rel="stylesheet">
<style>
:root{
  --ink:#1f1f1f;
  --text:#2a2a2a;
  --white:#ffffff;
  --footer-bg:#e9e9e9;
  --placeholder:#d9d9d9;
  --btn:#1f1f1f;
}
*{box-sizing:border-box;margin:0;padding:0}
html,body{width:831px;height:1200px;overflow:hidden;background:var(--white)}
body{position:relative;font-family:"Figtree",Arial,sans-serif;color:var(--text)}
.serif{font-family:"Lora",Georgia,serif;font-weight:400}
.abs{position:absolute}
.btn{position:absolute;background:var(--btn);color:var(--white);font-size:9.5px;font-weight:700;text-transform:uppercase;display:flex;align-items:center;justify-content:center;letter-spacing:.1px}

/* header */
.site-header{position:absolute;left:0;top:0;width:831px;height:58px;background:var(--white)}
.brand{left:52px;top:18px;font-size:20px;color:var(--ink)}
.nav{left:527px;top:22px;display:flex;gap:22px;font-size:9.5px;font-weight:600;color:var(--ink)}
.search{left:769px;top:22px}

/* hero */
.hero{position:absolute;left:0;top:58px;width:831px;height:388px;background:linear-gradient(100deg,#6b5a4c 0%,#cfc7bd 35%,#e3ddd6 60%,#a9a39c 100%)}
.newsletter-tab{position:absolute;left:0;top:248px;width:37px;height:170px;background:#1f1f1f;display:flex;align-items:center;justify-content:center}
.newsletter-tab span{color:var(--white);font-size:13px;writing-mode:vertical-rl;letter-spacing:.3px}
.hero-card{position:absolute;left:477px;top:180px;width:285px;height:136px;background:rgba(255,255,255,.68)}
.hero-title{left:32px;top:16px;font-size:36px;color:var(--ink)}
.hero-sub{left:32px;top:62px;font-size:11.5px;color:var(--ink)}
.hero-card .btn{left:32px;top:87px;width:72px;height:25px}
.scroll-down{position:absolute;left:398px;top:365px;width:34px;height:34px;border-radius:50%;background:var(--white);display:flex;align-items:center;justify-content:center}

/* services */
.service{position:absolute;top:486px;width:170px}
.service-icon{width:72px;height:72px;background:var(--placeholder)}
.service-title{margin-top:14px;font-size:12.5px;font-weight:700;color:var(--ink)}
.service-text{margin-top:9px;font-size:10px;line-height:15.3px;color:var(--text)}
.service .btn{position:relative;margin-top:15px;width:72px;height:25px}

/* welcome */
.welcome-title{left:55px;top:757px;font-size:20.5px;color:var(--ink)}
.welcome-copy{position:absolute;left:55px;top:794px;width:352px;font-size:9.7px;line-height:15.4px;text-align:justify;color:var(--text)}
.welcome-copy p+p{margin-top:15px}
.welcome-btn{left:52px;top:988px;width:73px;height:26px}
.welcome-photo{position:absolute;left:425px;top:745px;width:355px;height:256px;background:linear-gradient(180deg,#5d7f98 0%,#8b9aa4 45%,#c9a890 62%,#3b4550 72%,#1f2a33 100%)}

/* footer */
.site-footer{position:absolute;left:0;top:1038px;width:831px;height:162px;background:var(--footer-bg)}
.footer-brand{left:52px;top:30px;font-size:19px;color:var(--ink)}
.contact-line{position:absolute;left:52px;display:flex;align-items:center;gap:10px;font-size:8.5px;color:var(--ink)}
.small{font-size:8px;color:var(--ink)}
.footer-heading{font-size:13px;color:var(--ink)}
.quick-links{position:absolute;left:408px;top:65px;list-style:none}
.quick-links li{display:flex;align-items:center;gap:12px;font-size:8.5px;height:15.4px;color:var(--ink)}
.social{position:absolute;left:654px;top:62px;display:flex;gap:4px}
.social span{width:22px;height:22px;border-radius:50%;background:var(--white);display:block}
</style>
</head>
<body>

<header class="site-header">
  <div class="abs serif brand">Marendo Advisers Limited</div>
  <nav class="abs nav"><span>Home</span><span>About Us</span><span>Services</span><span>Contact Us</span></nav>
  <svg class="abs search" width="11" height="11" viewBox="0 0 11 11"><circle cx="4.5" cy="4.5" r="3.3" fill="none" stroke="#1f1f1f" stroke-width="1.6"/><line x1="7" y1="7" x2="10" y2="10" stroke="#1f1f1f" stroke-width="1.8" stroke-linecap="round"/></svg>
</header>

<section class="hero" role="img" aria-label="Photo of a smiling consultant in an office reviewing papers with a colleague">
  <div class="newsletter-tab"><span>Newsletter Subscribe</span></div>
  <div class="hero-card">
    <div class="abs serif hero-title">Lorium Ipsum</div>
    <div class="abs hero-sub">Vestibulum consectetuer suspendisse</div>
    <div class="btn">Read More</div>
  </div>
  <div class="scroll-down"><svg width="10" height="6" viewBox="0 0 10 6"><polyline points="1,1 5,5 9,1" fill="none" stroke="#1f1f1f" stroke-width="1.5"/></svg></div>
</section>

<section class="services">
  <article class="service" style="left:52px">
    <div class="service-icon" role="img" aria-label="Construction worker icon"></div>
    <h3 class="service-title">Construction</h3>
    <p class="service-text">Vivamus sed sed mauris erat metus. Pellentesque in nunc. Duis mattis ipsum vestibulum</p>
    <div class="btn">Read More</div>
  </article>
  <article class="service" style="left:242px">
    <div class="service-icon" role="img" aria-label="Lightning bolt energy icon"></div>
    <h3 class="service-title">Energy</h3>
    <p class="service-text">Vivamus sed sed mauris erat metus. Pellentesque in nunc. Duis mattis ipsum vestibulum</p>
    <div class="btn">Read More</div>
  </article>
  <article class="service" style="left:426px">
    <div class="service-icon" role="img" aria-label="Oil rig icon"></div>
    <h3 class="service-title">Oil and gas</h3>
    <p class="service-text">Vivamus sed sed mauris erat metus. Pellentesque in nunc. Duis mattis ipsum vestibulum</p>
    <div class="btn">Read More</div>
  </article>
  <article class="service" style="left:611px">
    <div class="service-icon" role="img" aria-label="Courthouse icon"></div>
    <h3 class="service-title">Legal professions</h3>
    <p class="service-text">Vivamus sed sed mauris erat metus. Pellentesque in nunc. Duis mattis ipsum vestibulum</p>
    <div class="btn">Read More</div>
  </article>
</section>

<section class="welcome">
  <h2 class="abs serif welcome-title">Welcome to Marendo Advisers Limited</h2>
  <div class="welcome-copy">
    <p>MAL is locally owned, founded and registered. Our shareholders are cultured Tanzanian citizens with extensive corporate experience in South Africa, Tanzania, United Kingdom and the United States.</p>
    <p>Our mission is to provide responsive and unrivalled professional advice from learned and experienced professionals versed in the local market, with an understanding of the cultural and logistical challenges faced by foreign investors.</p>
    <p>Our vision is to provide a complete investor’s package that initiates with company registration, compliance and documentation services and ultimately operational facilitation services.</p>
  </div>
  <div class="btn welcome-btn">Read More</div>
  <div class="welcome-photo" role="img" aria-label="Photo of an oil pipeline over water at sunset with cranes and a ship"></div>
</section>

<footer class="site-footer">
  <div class="abs serif footer-brand">Marendo Advisers Limited</div>
  <div class="contact-line" style="top:66px">
    <svg width="8" height="10" viewBox="0 0 8 10"><path d="M4 0a4 4 0 0 0-4 4c0 3 4 6 4 6s4-3 4-6a4 4 0 0 0-4-4z" fill="#1f1f1f"/><circle cx="4" cy="4" r="1.4" fill="#e9e9e9"/></svg>
    <span>Tanzanian</span>
  </div>
  <div class="contact-line" style="top:81px">
    <svg width="9" height="9" viewBox="0 0 9 9"><path d="M8.6 6.6 7 5.2c-.3-.2-.7-.2-1 .1l-.7.7C4.2 5.4 3.6 4.8 3 3.7l.7-.7c.3-.3.3-.7.1-1L2.4.4C2.1 0 1.6 0 1.3.3L.3 1.2C-.2 4.5 4.5 9.2 7.8 8.7l.9-1c.3-.3.3-.8-.1-1.1z" fill="#1f1f1f"/></svg>
    <span>Call Us: 1800-555-019</span>
  </div>
  <div class="abs small" style="left:51px;top:104px">© Copyright&nbsp; 2018</div>
  <div class="abs small" style="left:51px;top:121px;font-size:7.5px">www.marendoadvisers.com</div>

  <div class="abs serif footer-heading" style="left:408px;top:32px">Quick Links</div>
  <ul class="quick-links">
    <li><svg width="6" height="8" viewBox="0 0 6 8"><polyline points="1,1 4.5,4 1,7" fill="none" stroke="#1f1f1f" stroke-width="1.6"/></svg>Home</li>
    <li><svg width="6" height="8" viewBox="0 0 6 8"><polyline points="1,1 4.5,4 1,7" fill="none" stroke="#1f1f1f" stroke-width="1.6"/></svg>About Us</li>
    <li><svg width="6" height="8" viewBox="0 0 6 8"><polyline points="1,1 4.5,4 1,7" fill="none" stroke="#1f1f1f" stroke-width="1.6"/></svg>Services</li>
    <li><svg width="6" height="8" viewBox="0 0 6 8"><polyline points="1,1 4.5,4 1,7" fill="none" stroke="#1f1f1f" stroke-width="1.6"/></svg>Contact Us</li>
  </ul>

  <div class="abs serif footer-heading" style="left:655px;top:32px">Follow Us</div>
  <div class="social" aria-label="Social media links"><span></span><span></span><span></span><span></span><span></span></div>
</footer>

</body>
</html>
```